full stationary design for a modern sleek design company

we are a design company that does modern minimalistic interior design works as well as other design services for high end clients.
we need a full stationary design including and not limited to (double sided business card, letter head, envelopes, documents folder...etc) that reflects the modern style design we do.
sleek modern and minimalistic is the requirements.
Updates

please use the latest attached files as there was a slight modification on the logo Added Wednesday, March 1, 2017

minor update on the logo files in JPG and PSD has been updated kindly follow the new attachments. Added Thursday, March 2, 2017

Target Market(s)

modern minimalist clients

Industry/Entity Type

Design Agency

Requirements
Must have
• the logo
Nice to have
• i like the colors in the colored 3D logo attached
Should not have
• too many colors

```html
<!DOCTYPE html>
<html lang="en">
<head>
<meta charset="utf-8">
<title>Norde Studio — Stationery Set</title>
<link href="https://fonts.googleapis.com/css2?family=Lato:wght@400;700;900&family=Great+Vibes&display=swap" rel="stylesheet">
<style>
  :root {
    --backdrop: #d9dde8;
    --paper: #f2f2f2;
    --charcoal: #3e3e3e;
    --charcoal-deep: #353535;
    --orange: #e8891f;
    --ink: #2b2b2b;
    --ink-soft: #6a6a6a;
    --rule: #9a9a9a;
  }
  * { box-sizing: border-box; margin: 0; padding: 0; }
  html, body { width: 1200px; height: 1040px; overflow: hidden; background: var(--backdrop); }
  body { position: relative; font-family: "Lato", sans-serif; color: var(--ink); }

  .piece { position: absolute; background: var(--paper); overflow: hidden; }
  .piece--dark { background: var(--charcoal); color: #fff; }

  /* brand lockup */
  .brand { position: absolute; display: flex; align-items: flex-start; gap: 5px; }
  .brand__square { width: 9px; height: 9px; background: var(--orange); margin-top: 1px; }
  .brand__text { display: flex; flex-direction: column; }
  .brand__name { font-weight: 900; font-size: 10px; letter-spacing: 1.2px; text-transform: uppercase; color: var(--ink); line-height: 1; }
  .brand__by { font-size: 4.6px; letter-spacing: 2.4px; text-transform: uppercase; color: var(--orange); margin-top: 2px; }
  .piece--dark .brand__name { color: #fff; }

  .brand--large .brand__square { width: 22px; height: 22px; }
  .brand--large .brand__name { font-size: 22px; letter-spacing: 2px; }
  .brand--large .brand__by { font-size: 8px; letter-spacing: 4px; margin-top: 4px; }

  .brand--mid .brand__square { width: 14px; height: 14px; }
  .brand--mid .brand__name { font-size: 13px; }
  .brand--mid .brand__by { font-size: 5.5px; letter-spacing: 2.6px; }

  /* letter body */
  .letter__body { position: absolute; left: 24px; right: 24px; top: 84px; font-size: 5.3px; line-height: 7.8px; color: var(--ink-soft); }
  .letter__lead { font-weight: 700; color: var(--ink); margin-bottom: 8px; }
  .letter__body p + p { margin-top: 7px; }

  .contact { position: absolute; border-left: 2px solid var(--orange); padding-left: 5px; font-size: 4.2px; line-height: 5.6px; color: var(--ink); }

  /* envelope back */
  .envelope-back__flap { position: absolute; left: 0; top: 0; width: 100%; height: 36px; }

  /* CD */
  .disc { position: absolute; border-radius: 50%; background: var(--paper); border: 3px solid #b9bcc4; }
  .disc__hole { position: absolute; left: 50%; top: 50%; width: 20px; height: 20px; margin: -10px 0 0 -10px; border-radius: 50%; background: var(--backdrop); border: 4px solid #e2e2e2; }
  .disc__field { position: absolute; font-size: 5px; color: var(--ink-soft); display: flex; gap: 4px; align-items: flex-end; }
  .disc__line { width: 48px; border-bottom: 0.6px solid var(--rule); }

  .slip__sign { position: absolute; right: 18px; bottom: 14px; font-family: "Great Vibes", cursive; font-size: 14px; color: var(--ink); }

  .card__url { position: absolute; left: 0; right: 0; bottom: 6px; text-align: center; font-size: 3.4px; color: #bbb; }
  .card__band { position: absolute; left: 0; right: 0; bottom: 0; height: 24px; background: var(--charcoal); color: #fff; }
  .card__person { position: absolute; left: 7px; top: 9px; font-size: 4px; font-weight: 700; line-height: 5px; }
  .card__role { color: var(--orange); font-weight: 400; font-size: 3.2px; }
  .card__address { position: absolute; left: 66px; top: 3px; font-size: 2.8px; line-height: 3.6px; color: #ccc; }
  .card__details { position: absolute; left: 66px; top: 12px; border-left: 1px solid var(--orange); padding-left: 2px; font-size: 2.8px; line-height: 3.4px; color: #ddd; }

  .folder__url { position: absolute; left: 0; right: 0; bottom: 26px; text-align: center; font-size: 7.5px; letter-spacing: 0.6px; color: #ddd; }
</style>
</head>
<body>

  <!-- Letterhead, left -->
  <section class="piece letterhead" style="left:106px;top:65px;width:274px;height:383px;">
    <div class="brand" style="left:28px;top:27px;">
      <span class="brand__square"></span>
      <span class="brand__text"><span class="brand__name">Norde Studio</span><span class="brand__by">by Elias Varenne</span></span>
    </div>
    <div class="letter__body" style="top:84px;">
      <p class="letter__lead">Lorem ipsum dolor sit amet, consectetur adipiscing elit. Quisque convallis, risus nec malesuada posuere, ligula sem varius mi, id tincidunt tortor sem quis lectus. Sed gravida tellus id nulla commodo volutpat.</p>
      <p>Morbi vel efficitur sapien. Duis tempor, nisi ullamcorper ullamcorper venenatis, diam quam rhoncus mauris, vel venenatis velit dui id lectus. Aenean non orci eleifend, elementum lectus vel, tempus ipsum. Ut efficitur facilisis pulvinar. Pellentesque habitant morbi tristique senectus et netus et malesuada fames ac turpis egestas. Vivamus varius, risus eu varius elementum, risus felis accumsan metus, laoreet blandit magna magna a nisl.</p>
      <p>Proin consequat dapibus diam, sit amet pharetra orci vestibulum eget. Fusce efficitur ante et justo tempus posuere et a purus. In luctus ligula augue, non viverra elit dapibus eu. Maecenas augue massa, tincidunt eget egestas a, pellentesque vitae justo. In nunc augue, blandit ac vulputate eget, pretium ut sapien. Duis volutpat sagittis nunc, blandit sagittis nisl mollis sed.</p>
      <p>Donec dui diam, faucibus non consectetur in, fermentum non neque. Cras fringilla vitae odio rhoncus gravida. Sed magna arcu, tempor nec tortor bibendum, aliquam scelerisque erat. Duis suscipit urna non massa feugiat lacinia. Aenean eu augue interdum, accumsan justo ut, laoreet lectus.</p>
      <p>Proin consequat dapibus diam, sit amet pharetra orci vestibulum eget. Fusce efficitur ante et justo tempus posuere et a purus. In nunc augue, blandit ac vulputate eget, pretium ut sapien.</p>
    </div>
    <div class="contact" style="left:22px;bottom:13px;">000 . 1234 . 5678<br>hello@nordestudio.com<br>www.nordestudio.com</div>
  </section>

  <!-- Envelope front -->
  <section class="piece envelope-front" style="left:441px;top:130px;width:286px;height:142px;">
    <div class="brand" style="left:20px;top:15px;">
      <span class="brand__square"></span>
      <span class="brand__text"><span class="brand__name">Norde Studio</span><span class="brand__by">by Elias Varenne</span></span>
    </div>
    <div class="contact" style="left:14px;bottom:16px;">000 . 1234 . 5678<br>hello@nordestudio.com<br>www.nordestudio.com</div>
  </section>

  <!-- Envelope back -->
  <section class="piece envelope-back" style="left:745px;top:128px;width:286px;height:142px;">
    <svg class="envelope-back__flap" viewBox="0 0 286 36" preserveAspectRatio="none" aria-hidden="true">
      <polygon points="0,0 286,0 286,2 272,35 14,35 0,2" fill="var(--charcoal)"/>
    </svg>
    <span class="brand__square" style="position:absolute;left:138px;top:13px;"></span>
  </section>

  <!-- Document folder -->
  <section class="piece piece--dark folder" style="left:105px;top:520px;width:273px;height:383px;">
    <div class="brand brand--large" style="left:50px;top:150px;flex-direction:column;align-items:center;gap:10px;width:173px;">
      <span class="brand__square"></span>
      <span class="brand__text" style="align-items:center;"><span class="brand__name">Norde Studio</span><span class="brand__by">by Elias Varenne</span></span>
    </div>
    <div class="folder__url">www.nordestudio.com</div>
  </section>

  <!-- Letterhead, centre -->
  <section class="piece letterhead" style="left:449px;top:332px;width:274px;height:384px;">
    <div class="brand" style="left:28px;top:27px;">
      <span class="brand__square"></span>
      <span class="brand__text"><span class="brand__name">Norde Studio</span><span class="brand__by">by Elias Varenne</span></span>
    </div>
    <div class="letter__body" style="top:84px;">
      <p class="letter__lead">Lorem ipsum dolor sit amet, consectetur adipiscing elit. Quisque convallis, risus nec malesuada posuere, ligula sem varius mi, id tincidunt tortor sem quis lectus. Sed gravida tellus id nulla commodo volutpat.</p>
      <p>Morbi vel efficitur sapien. Duis tempor, nisi ullamcorper ullamcorper venenatis, diam quam rhoncus mauris, vel venenatis velit dui id lectus. Aenean non orci eleifend, elementum lectus vel, tempus ipsum. Ut efficitur facilisis pulvinar. Pellentesque habitant morbi tristique senectus et netus et malesuada fames ac turpis egestas. Vivamus varius, risus eu varius elementum, risus felis accumsan metus, laoreet blandit magna magna a nisl.</p>
      <p>Proin consequat dapibus diam, sit amet pharetra orci vestibulum eget. Fusce efficitur ante et justo tempus posuere et a purus. In luctus ligula augue, non viverra elit dapibus eu. Maecenas augue massa, tincidunt eget egestas a, pellentesque vitae justo. In nunc augue, blandit ac vulputate eget, pretium ut sapien. Duis volutpat sagittis nunc, blandit sagittis nisl mollis sed.</p>
      <p>Donec dui diam, faucibus non consectetur in, fermentum non neque. Cras fringilla vitae odio rhoncus gravida. Sed magna arcu, tempor nec tortor bibendum, aliquam scelerisque erat. Duis suscipit urna non massa feugiat lacinia. Aenean eu augue interdum, accumsan justo ut, laoreet lectus.</p>
      <p>Proin consequat dapibus diam, sit amet pharetra orci vestibulum eget. Fusce efficitur ante et justo tempus posuere et a purus. In nunc augue, blandit ac vulputate eget, pretium ut sapien.</p>
    </div>
    <div class="contact" style="left:22px;bottom:13px;">000 . 1234 . 5678<br>hello@nordestudio.com<br>www.nordestudio.com</div>
  </section>

  <!-- CD sleeve -->
  <section class="piece piece--dark sleeve" style="left:782px;top:336px;width:163px;height:160px;">
    <div class="brand brand--mid" style="left:0;top:54px;width:163px;flex-direction:column;align-items:center;gap:7px;">
      <span class="brand__square"></span>
      <span class="brand__text" style="align-items:center;"><span class="brand__name">Norde Studio</span><span class="brand__by">by Elias Varenne</span></span>
    </div>
  </section>

  <!-- CD -->
  <section class="disc" style="left:785px;top:531px;width:154px;height:154px;">
    <div class="disc__field" style="left:38px;top:33px;">Project <span class="disc__line"></span></div>
    <div class="disc__field" style="left:48px;top:46px;">Date <span class="disc__line" style="width:40px;"></span></div>
    <div class="disc__hole"></div>
    <span class="brand__square" style="position:absolute;left:68px;top:113px;width:12px;height:12px;"></span>
  </section>

  <!-- Compliment slip -->
  <section class="piece slip" style="left:450px;top:767px;width:273px;height:127px;">
    <div class="brand brand--mid" style="left:16px;top:16px;">
      <span class="brand__square"></span>
      <span class="brand__text"><span class="brand__name">Norde Studio</span><span class="brand__by">by Elias Varenne</span></span>
    </div>
    <div class="slip__sign">With Compliments</div>
  </section>

  <!-- Business cards, fronts -->
  <section class="piece piece--dark card" style="left:786px;top:719px;width:118px;height:64px;">
    <span class="brand__square" style="position:absolute;left:53px;top:22px;width:12px;height:12px;"></span>
    <div class="card__url">www.nordestudio.com</div>
  </section>
  <section class="piece card" style="left:938px;top:719px;width:118px;height:64px;background:var(--charcoal-deep);">
    <span class="brand__square" style="position:absolute;left:53px;top:26px;width:12px;height:12px;background:#4a3a26;"></span>
  </section>

  <!-- Business cards, backs -->
  <section class="piece card" style="left:788px;top:826px;width:117px;height:64px;">
    <div class="brand" style="left:13px;top:12px;">
      <span class="brand__text" style="align-items:center;"><span class="brand__name" style="font-size:8px;">Norde Studio</span><span class="brand__by" style="font-size:4px;">by Elias Varenne</span></span>
    </div>
    <div class="card__band">
      <div class="card__person">OWEN HALE<br><span class="card__role">Graphic Designer</span></div>
      <div class="card__address">12 Harbor Lane, Suite 4<br>Springfield 00000</div>
      <div class="card__details">000 . 1234 . 5678<br>hello@nordestudio.com<br>www.nordestudio.com</div>
    </div>
  </section>
  <section class="piece card" style="left:940px;top:826px;width:117px;height:64px;">
    <div class="brand" style="left:13px;top:12px;">
      <span class="brand__text" style="align-items:center;"><span class="brand__name" style="font-size:8px;">Norde Studio</span><span class="brand__by" style="font-size:4px;">by Elias Varenne</span></span>
    </div>
    <div class="card__band">
      <div class="card__person">OWEN HALE<br><span class="card__role">Graphic Designer</span></div>
      <div class="card__address">12 Harbor Lane, Suite 4<br>Springfield 00000</div>
      <div class="card__details">000 . 1234 . 5678<br>hello@nordestudio.com<br>www.nordestudio.com</div>
    </div>
  </section>

</body>
</html>
```